Health Information/Education Logo Design

We need a logo design for a new company based in Atlanta called Meadowlark Health. The program is about patient empowerment. We provide health information and education on how to get healthy, stay healthy, and how to be proactive in your care. We also provide medication and injection training to help patients feel their best and to ensure successful therapy outcomes.
We like the colors yellow, pink, teal and purple and would like to see some or all of these colors in the designs. The final design should communicate caring, considerate, compassionate information, education and training services
Industry/Entity Type
Education
Contact Information for Business Card
Meadowlark Health
Danielle Ostrander RN, MSN, MHA
Nurse Educator
555.214.3096 cell
555.470.2283 fax

```html
<!DOCTYPE html>
<html lang="en">
<head>
<meta charset="utf-8">
<title>Meadowlark Health – Business Card</title>
<link rel="stylesheet" href="https://fonts.googleapis.com/css2?family=Iceland&family=Orbitron:wght@400;500&display=swap">
<style>
  :root {
    --card-yellow: #eefe1b;
    --card-purple: #6a1bff;
    --card-pink: #ff10ee;
    --text-yellow: #f2ff1b;
    --page-white: #ffffff;
  }
  html, body {
    margin: 0;
    padding: 0;
    width: 1200px;
    height: 699px;
    overflow: hidden;
    background: var(--page-white);
  }
  .card {
    position: relative;
    width: 1200px;
    height: 699px;
  }
  .card-shapes {
    position: absolute;
    inset: 0;
  }
  .brand {
    position: absolute;
    left: 60px;
    top: 220px;
    width: 500px;
    text-align: center;
  }
  .brand-dot {
    width: 170px;
    height: 170px;
    margin: 0 auto 50px;
    border-radius: 50%;
    background: var(--card-purple);
  }
  .brand-name {
    margin: 0;
    font-family: "Orbitron", sans-serif;
    font-weight: 400;
    font-size: 30px;
    letter-spacing: 2px;
    color: var(--card-purple);
    text-transform: uppercase;
  }
  .person {
    position: absolute;
    left: 640px;
    top: 140px;
    width: 520px;
    text-align: center;
    color: var(--text-yellow);
  }
  .person-name {
    margin: 0;
    font-family: "Iceland", sans-serif;
    font-weight: 400;
    font-size: 56px;
    line-height: 1;
    text-align: right;
  }
  .person-degrees {
    margin: 14px 0 0;
    font-family: "Orbitron", sans-serif;
    font-size: 20px;
    letter-spacing: 2px;
  }
  .person-role {
    margin: 6px 0 0 -20px;
    font-family: "Orbitron", sans-serif;
    font-size: 30px;
    letter-spacing: 3px;
  }
  .contact {
    position: absolute;
    left: 664px;
    top: 425px;
    margin: 0;
    padding: 0;
    list-style: none;
    font-family: "Orbitron", sans-serif;
    font-size: 33px;
    letter-spacing: 3px;
    line-height: 50px;
    color: var(--text-yellow);
  }
</style>
</head>
<body>
  <main class="card">
    <svg class="card-shapes" width="1200" height="699" viewBox="0 0 1200 699" aria-hidden="true">
      <defs>
        <clipPath id="card-outline">
          <rect x="10" y="10" width="1180" height="675" rx="34" ry="34"/>
        </clipPath>
      </defs>
      <g clip-path="url(#card-outline)">
        <rect x="0" y="0" width="1200" height="699" fill="var(--card-purple)"/>
        <path d="M0,0 L554,0 L554,10 C680,160 720,440 470,699 L0,699 Z" fill="var(--card-pink)"/>
        <path d="M0,0 L554,0 L554,10 C650,160 690,420 404,699 L0,699 Z" fill="var(--card-yellow)"/>
      </g>
    </svg>

    <section class="brand">
      <div class="brand-dot"></div>
      <p class="brand-name">Meadowlark Health</p>
    </section>

    <section class="person">
      <h1 class="person-name">Danielle Ostrander, RN</h1>
      <p class="person-degrees">MSN, MHA</p>
      <p class="person-role">Nurse Educator</p>
    </section>

    <ul class="contact">
      <li class="contact-cell">Cell : 555.214.3096</li>
      <li class="contact-fax">Fax : 555.470.2283</li>
    </ul>
  </main>
</body>
</html>
```